Brandt Family Motto/Mission Statement

We are creating a poster to be hung in our home with several purpose statements for our family (last name Brandt, and "The Brandt Family" should be included in the poster prominently). The text that we want included is in the attached file.

Our kids range in age from 8 to 17, so we are looking for something that is homey and cheerful, but fairly bold and oriented to older kids (and not so much younger kids).

I've attached a couple of example poster/statements that we generally like. Overall color scheme could include blues and greens and possibly some brown.

Anticipated size of this poster would be 18"x24" with a portrait orientation.

```html
<!DOCTYPE html>
<html lang="en">
<head>
<meta charset="utf-8">
<title>The Brandt Family – Our Values</title>
<link href="https://fonts.googleapis.com/css2?family=Baloo+2:wght@800&display=swap" rel="stylesheet">
<style>
  :root {
    --navy: #0b0b6b;
    --glow: #ffffff;
    --rule: rgba(120, 150, 200, 0.45);
    --frame: #4a4f5c;
    --bg-top: #7d98c8;
    --bg-mid: #dfe5ef;
    --bg-light: #f4f6fa;
    --bg-low: #c9d1de;
  }
  html, body {
    margin: 0;
    padding: 0;
    width: 902px;
    height: 1200px;
    overflow: hidden;
    background: #ffffff;
  }
  .poster {
    position: relative;
    width: 902px;
    height: 1200px;
    box-sizing: border-box;
    border: 1.5px solid var(--frame);
    overflow: hidden;
    font-family: "Baloo 2", "Trebuchet MS", sans-serif;
    font-weight: 800;
    color: var(--navy);
  }
  .backdrop {
    position: absolute;
    inset: 0;
    background:
      radial-gradient(ellipse at 100% 0%, var(--bg-top) 0%, rgba(125,152,200,0.55) 22%, rgba(223,229,239,0) 50%),
      radial-gradient(ellipse at 0% 85%, var(--bg-low) 0%, rgba(201,209,222,0) 55%),
      linear-gradient(160deg, var(--bg-mid) 0%, var(--bg-light) 45%, var(--bg-mid) 100%);
  }
  .value-line {
    position: absolute;
    left: 0;
    right: 0;
    text-align: center;
    font-size: 35px;
    line-height: 44px;
    letter-spacing: -0.2px;
    white-space: nowrap;
    text-shadow: 0 0 4px var(--glow), 0 0 8px var(--glow), 0 0 2px var(--glow);
  }
  .divider {
    position: absolute;
    left: 190px;
    width: 512px;
    height: 3px;
    background: var(--rule);
    border-radius: 2px;
  }
  .brand-rule {
    position: absolute;
    left: 133px;
    width: 633px;
    height: 2px;
    background: var(--rule);
  }
  .family-name {
    position: absolute;
    left: 0;
    right: 0;
    top: 1030px;
    text-align: center;
    font-size: 86px;
    line-height: 100px;
    letter-spacing: -1.5px;
    white-space: nowrap;
    text-shadow: 0 0 6px var(--glow), 0 0 12px var(--glow);
  }
  .family-name .article {
    display: inline-block;
    font-size: 30px;
    transform: rotate(-90deg) translate(14px, -4px);
    margin-right: -6px;
    vertical-align: middle;
  }
</style>
</head>
<body>
<main class="poster">
  <div class="backdrop" role="img" aria-label="Soft abstract background of pale blue glassy tiles and a faint grid with scattered numerals"></div>

  <div class="value-line" style="top:88px">We love</div>
  <div class="value-line" style="top:133px">to LEARN new things.</div>
  <div class="divider" style="top:199px"></div>

  <div class="value-line" style="top:222px">We look at life</div>
  <div class="value-line" style="top:266px">through a POSITIVE lens.</div>
  <div class="divider" style="top:329px"></div>

  <div class="value-line" style="top:350px">KINDNESS guides</div>
  <div class="value-line" style="top:394px">our words and deeds.</div>
  <div class="divider" style="top:448px"></div>

  <div class="value-line" style="top:470px">We create ADVENTURE</div>
  <div class="value-line" style="top:514px">and choose</div>
  <div class="value-line" style="top:558px">experiences over things.</div>
  <div class="divider" style="top:619px"></div>

  <div class="value-line" style="top:641px">We commit to be FIT.</div>
  <div class="divider" style="top:701px"></div>

  <div class="value-line" style="top:713px">Our days</div>
  <div class="value-line" style="top:758px">are brightened</div>
  <div class="value-line" style="top:802px">BY A SENSE OF HUMOR.</div>
  <div class="divider" style="top:857px"></div>

  <div class="value-line" style="top:879px">We DO WHAT IS RIGHT</div>
  <div class="value-line" style="top:925px">even when no one is watching.</div>

  <div class="brand-rule" style="top:1029px"></div>
  <h1 class="family-name" style="margin:0;font-weight:800"><span class="article">The</span>Brandt Family</h1>
  <div class="brand-rule" style="top:1135px"></div>
</main>
</body>
</html>
```